Elite boxing brochure

I need a brochure for a boxing training camp please. I would like it to look like the imagery on our Desmond Rourke website http://www.rourkeringcamp.example/ . I have attached some images and the text to be included. The final design needs to attract High net worth individuals, and communicate exclusivity. many thanks. Glen. Please feel free to copy any images from our Rourke website- we have the license to use any and all images on that site

```html
<!DOCTYPE html>
<html lang="en">
<head>
<meta charset="utf-8">
<title>Desmond Rourke Elite Boxing Camp</title>
<link href="https://fonts.googleapis.com/css2?family=Oswald:wght@500;600&family=Roboto+Slab:wght@300;400;800&display=swap" rel="stylesheet">
<style>
:root{
  --red:#e8313a;
  --red-deep:#b51f27;
  --ink:#231f20;
  --ink-soft:#3a3434;
  --white:#ffffff;
}
*{margin:0;padding:0;box-sizing:border-box}
html,body{width:839px;height:1200px;overflow:hidden;background:var(--ink)}
.brochure{
  position:relative;width:839px;height:1200px;overflow:hidden;color:var(--white);
  font-family:"Roboto Slab",serif;font-weight:300;
  background:linear-gradient(162deg,var(--red) 0%,#e02c35 40%,var(--red-deep) 58%,#4a2224 72%,var(--ink) 84%);
}
.display{font-family:"Oswald",sans-serif;font-weight:600;letter-spacing:.2px}
.abs{position:absolute;white-space:nowrap}

.extras-title{left:64px;top:42px;font-size:16px;line-height:20px}
.extras{left:48px;top:68px;list-style:none;font-size:13px}
.extras li{height:24.7px;line-height:24.7px}
.extras li::before{content:"★";font-size:12px;margin-right:6px}

.portrait{left:650px;top:18px;width:180px;height:196px;background:radial-gradient(ellipse at 50% 55%,var(--ink) 0%,var(--ink) 45%,rgba(35,31,32,0) 72%)}

.agenda-tab{left:45px;top:223px;width:152px;height:40px;background:var(--ink);clip-path:polygon(0 0,88% 0,100% 100%,0 100%)}
.agenda-tab span{position:absolute;left:44px;top:6px;font-size:18px;line-height:24px}
.agenda{left:32px;top:262px;width:776px;height:223px;background:var(--ink)}
.agenda .divider{position:absolute;left:259px;top:0;width:1px;height:223px;background:var(--ink-soft)}
.day{position:absolute;top:9px;font-size:13.4px;white-space:nowrap}
.day h3{font-family:"Oswald",sans-serif;font-weight:600;font-size:15.5px;line-height:20px}
.day ul{list-style:none}
.day li{line-height:17.6px}
.day li::before{content:"• "}
.day .evening{position:absolute;left:0;line-height:19px}
.day b{font-weight:800;font-size:14.5px}
.day-1{left:32px}.day-2{left:272px}.day-3{left:560px}

.section-title{font-size:15.5px;line-height:20px}
.workshops{left:64px;top:504px}
.lectures{left:455px;top:504px}
.points{list-style:none;font-size:12.8px}
.points li{position:relative}
.points li::before{content:"";position:absolute;left:-19px;top:6px;width:13px;height:6px;background:var(--white);clip-path:polygon(0 25%,62% 25%,62% 0,100% 50%,62% 100%,62% 75%,0 75%)}
.workshops .points li{line-height:16.65px}
.lectures .points li{line-height:17.1px}
.points b{font-weight:800}
.points .indent{padding-left:85px}
.points .indent-small{padding-left:32px}
.must-take{margin-top:15px;font-size:12.8px;line-height:17px}

.sparring-note{left:64px;top:806px;font-size:12px;line-height:18px}
.fight{left:64px;top:847px;font-size:12.8px;line-height:18.5px}
.fight h2{margin-bottom:1px}
.who{left:64px;top:919px;font-size:12.3px;line-height:16.3px}
.who h2{margin-bottom:2px}

.date{left:0;width:839px;top:1055px;text-align:center;font-size:20px;line-height:28px}
.cost{left:264px;top:1096px;width:310px;height:36px;border-radius:18px;background:var(--red);text-align:center;font-size:22px;line-height:36px}
.glove{top:1099px;width:62px;height:31px;border-radius:8px;background:var(--red)}
.glove-left{left:194px}.glove-right{left:583px}
.contact{left:0;width:839px;top:1147px;text-align:center;font-size:19.5px;line-height:28px}
</style>
</head>
<body>
<main class="brochure">
  <h2 class="abs display extras-title">In addition we will provide you with</h2>
  <ul class="abs extras">
    <li>A Personalised training plan for 6 months</li>
    <li>A personalised action plan to improve technique</li>
    <li>A personalised video showcasing your training to show to your friends and family</li>
    <li>Desmond Rourke Branded Folder for your own notes</li>
    <li>Desmond Rourke Certified plaque</li>
  </ul>
  <div class="abs portrait" role="img" aria-label="Dark silhouette portrait of the boxer"></div>

  <div class="abs agenda-tab"><span class="display">Agenda</span></div>
  <section class="abs agenda">
    <div class="divider"></div>
    <div class="day day-1">
      <h3>Day 1 &nbsp;Thursday 16th April</h3>
      <ul><li>Introductions</li><li>Technical Workshops</li><li>Explanation Lectures</li><li>Lunch</li><li>Technical Workshops</li><li>Fight Analysis</li><li>Technical Workshops</li></ul>
      <p class="evening" style="top:144px"><b>Evening:</b> &nbsp;Watch some of the<br>best fights of all time ,</p>
    </div>
    <div class="day day-2">
      <h3>Day 2Friday 17th April</h3>
      <ul><li>Technical Workshops</li><li>Explanation Lectures</li><li>Lunch</li><li>Technical Workshops</li><li>Fight Analysis</li><li>Technical Workshops</li></ul>
      <p class="evening" style="top:128px"><b>Evening:</b> &nbsp;Watch some of the best<br>fights of all time , boxing trivia quiz</p>
    </div>
    <div class="day day-3">
      <h3>Day 3 &nbsp;Saturday 18th April</h3>
      <ul><li>Technical Workshops</li><li>Explanation Lectures</li><li>Lunch</li><li>Technical Workshops</li><li>Fight Analysis</li><li>Technical Workshops</li></ul>
      <p class="evening" style="top:128px"><b>Evening</b> Depart</p>
    </div>
  </section>

  <section class="abs workshops">
    <h2 class="display section-title">Technical Workshops will cover:</h2>
    <ul class="points">
      <li>Sparring,</li><li>Technical training</li><li>Correct footwork</li><li>Punching harder workshop</li><li>Balance</li><li>The art of Forcing a stoppage in a fight</li><li>Technical drills-</li><li>Varying the jab to confuse your opponent &nbsp;4 types</li><li>Points – outscoring your opponent</li><li>Defensive work- the duck slip and swayback</li><li>Combination punching</li><li>Coping strategies for when you are hurt and fatigued</li><li>How to beat a taller / shorter fighter than you</li><li>Power v endurance</li><li>Sustained attacks and counting</li><li>Punch counting</li>
    </ul>
  </section>

  <section class="abs lectures">
    <h2 class="display section-title">Explanation Lectures will cover:</h2>
    <ul class="points">
      <li><b>Physiology:</b> The bodys energy systems and how<br><span class="indent">they relate to boxing</span></li>
      <li><b>Physiology:</b> Measuring progress</li>
      <li><b>Biomechanics:</b> Punching for power</li>
      <li><b>Biomechanics:</b> Correct footwork</li>
      <li><b>Psychology:</b> The inverted U</li>
      <li><b>Psychology:</b> &nbsp;Skill acquisition and interference from<br><span class="indent-small">practice to sparring to competition</span></li>
      <li><b>Psychology:</b>Visualisation</li>
      <li><b>Training through injury</b> - training your energy<br>systems not just using boxing</li>
    </ul>
    <p class="must-take">The 11 things you MUST take to a boxing ring</p>
  </section>

  <p class="abs sparring-note">(Sparring is optional and will be very carefully controlled.)</p>

  <section class="abs fight">
    <h2 class="display section-title">Fight analysis</h2>
    <p>Review the greatest fights and fighters,<br>learn their moves and how you could beat them</p>
  </section>

  <section class="abs who">
    <h2 class="display section-title">Who should come?</h2>
    <p>This is an ELITE boxing training camp designed to equip you with knowledge, the skills and a training<br>program to improve massively over a 6 month period. We GUARANTEE your &nbsp;mprovement if you stick to<br>the program AND eat healthy. &nbsp;You have an opportunity to work with the very best in the world so please<br>be open minded and be prepared to learn. You should come if you want a structured, individualised<br>program of improvement GUARANTEED to work for YOU.</p>
  </section>

  <p class="abs display date">Date 16-18th April 2015 | Venue: addres here</p>
  <div class="abs glove glove-left" role="img" aria-label="Red boxing glove illustration"></div>
  <p class="abs display cost">Cost &nbsp;&nbsp;US $ 3000 per person</p>
  <div class="abs glove glove-right" role="img" aria-label="Red boxing glove illustration"></div>
  <p class="abs display contact">Contact Mr Corin Velasquez+971 50 000 1234 &nbsp;email: &nbsp;corin@ringform.example &nbsp;to book</p>
</main>
</body>
</html>
```